Criação de Papelaria Profissional para Brumado & Lúmen
" Buscamos soluções de TI sob medida para o negócio do cliente. Temos um slogan. "TI a serviço do seu negócio". o melhor briefing está aqui https://brivantesistemas.com.br/sobre/ "

```html
<!DOCTYPE html>
<html lang="pt-BR">
<head>
<meta charset="utf-8">
<title>Assinatura de e-mail – Brumado &amp; Lúmen</title>
<link rel="stylesheet" href="https://fonts.googleapis.com/css2?family=Montserrat:wght@400;500;700&display=swap">
<style>
  :root {
    --bg-orange: #f58634;
    --brand-orange: #f0862e;
    --card: #ffffff;
    --ink: #3c3c3c;
    --ink-soft: #555555;
    --badge: #dcdcdc;
    --photo-a: #e9e4df;
    --photo-b: #2b2b2f;
  }
  * { box-sizing: border-box; margin: 0; padding: 0; }
  html, body { width: 1200px; height: 1200px; overflow: hidden; }
  body {
    background: var(--bg-orange);
    font-family: "Montserrat", Arial, sans-serif;
    color: var(--ink);
    position: relative;
  }
  .signature {
    position: absolute;
    left: 34px; top: 468px;
    width: 1132px; height: 290px;
    background: var(--card);
    box-shadow: 0 6px 12px rgba(0,0,0,0.18);
  }
  .portrait {
    position: absolute;
    left: 63px; top: 44px;
    width: 200px; height: 200px;
    border-radius: 50%;
    background: linear-gradient(180deg, var(--photo-a) 0%, var(--photo-a) 55%, var(--photo-b) 100%);
  }
  .identity { position: absolute; left: 300px; top: 44px; }
  .identity .name { font-weight: 700; font-size: 25px; letter-spacing: 0.3px; }
  .identity .role { font-size: 21px; color: var(--ink-soft); margin-top: 2px; }
  .brand { margin-top: 22px; }
  .brand .brand-name {
    font-weight: 700; font-size: 32px; color: var(--brand-orange); line-height: 1;
  }
  .brand .slogan { font-size: 12px; color: var(--brand-orange); margin-top: 6px; }
  .partner-badge {
    margin-top: 20px;
    width: 220px; height: 42px;
    border-radius: 3px;
    background: var(--badge);
  }
  .contacts {
    position: absolute; left: 700px; top: 54px;
    list-style: none; font-size: 20px;
  }
  .contacts li { display: flex; align-items: flex-start; margin-bottom: 10px; line-height: 1.05; }
  .contacts svg { width: 18px; height: 18px; margin: 2px 10px 0 0; flex: none; fill: var(--brand-orange); }
  .social { display: flex; gap: 14px; margin-top: 18px; }
  .social span { width: 38px; height: 38px; border-radius: 50%; background: var(--brand-orange); }
</style>
</head>
<body>
  <section class="signature">
    <div class="portrait" role="img" aria-label="Foto de retrato profissional do colaborador"></div>

    <div class="identity">
      <p class="name">NOME E SOBRENOME</p>
      <p class="role">Cargo | Função</p>
      <div class="brand">
        <p class="brand-name">Brumado &amp; Lúmen</p>
        <p class="slogan">TI a serviço do seu negócio</p>
      </div>
      <div class="partner-badge" role="img" aria-label="Selo de parceiro"></div>
    </div>

    <ul class="contacts">
      <li>
        <svg viewBox="0 0 24 24"><path d="M6.6 10.8a15.1 15.1 0 0 0 6.6 6.6l2.2-2.2c.3-.3.7-.4 1-.2 1.1.4 2.3.6 3.6.6.6 0 1 .4 1 1V20c0 .6-.4 1-1 1A17 17 0 0 1 3 4c0-.6.4-1 1-1h3.5c.6 0 1 .4 1 1 0 1.3.2 2.5.6 3.6.1.3 0 .7-.2 1z"/></svg>
        <span>(11) 3870-2256</span>
      </li>
      <li>
        <svg viewBox="0 0 24 24"><path d="M2 5h20v14H2z M2 5l10 8 10-8" /></svg>
        <span>contato@brumadolumen.com.br</span>
      </li>
      <li>
        <svg viewBox="0 0 24 24"><path d="M12 2a10 10 0 1 0 0 20 10 10 0 0 0 0-20zm0 2c1 0 2.3 2 2.8 5H9.2C9.7 6 11 4 12 4zM4.3 11h3a17 17 0 0 0 0 2h-3a8 8 0 0 1 0-2zm5 0h5.4a15 15 0 0 1 0 2H9.3a15 15 0 0 1 0-2zm7.4 0h3a8 8 0 0 1 0 2h-3a17 17 0 0 0 0-2zM9.2 15h5.6c-.5 3-1.8 5-2.8 5s-2.3-2-2.8-5z"/></svg>
        <span>www.brumadolumen.com.br</span>
      </li>
      <li>
        <svg viewBox="0 0 24 24"><path d="M12 2a7 7 0 0 0-7 7c0 5 7 13 7 13s7-8 7-13a7 7 0 0 0-7-7zm0 9.5A2.5 2.5 0 1 1 12 6.5a2.5 2.5 0 0 1 0 5z"/></svg>
        <span>Rua das Acácias, 845 cj.<br>7 B - Vila Aurora São Paulo/SP</span>
      </li>
      <li class="social" aria-label="Redes sociais">
        <span></span><span></span><span></span><span></span>
      </li>
    </ul>
  </section>
</body>
</html>
```